Business Card Design for a Personal Trainer

I need a business card design for my job as a personal trainer. It should have a unique, modern and exclusive design. On the front there should be only my logo with my name and my job. 0163/2918374 Tobias Kellinger Lindenfeldweg 14 80412 Munich Germany The most important contact information is the web adress. it can be bigger than the rest, but its not necessary. The card should be 8,5cmx5,5cm big. Font: Roboto. Colors: black, white, gray, 56c1ff.

```html
<!DOCTYPE html>
<html lang="de">
<head>
<meta charset="utf-8">
<title>Tobias Kellinger – Personal Trainer Visitenkarte</title>
<link rel="stylesheet" href="https://fonts.googleapis.com/css2?family=Roboto:wght@300;400;700&display=swap">
<style>
  :root {
    --page: #e9eaeb;
    --card-dark: #252525;
    --card-darker: #161616;
    --accent: #8cc0ea;
    --accent-light: #a6cff0;
    --white: #ffffff;
    --text-light: #e4e4e4;
    --photo-mid: #5a5a5a;
    --photo-dark: #2e2e2e;
  }
  * { box-sizing: border-box; margin: 0; padding: 0; }
  html, body {
    width: 1200px; height: 969px; overflow: hidden;
    background: var(--page);
    font-family: "Roboto", Arial, sans-serif;
  }
  .canvas { position: relative; width: 1200px; height: 969px; }

  .card {
    position: absolute; width: 560px; height: 362px;
    overflow: hidden; border-radius: 3px;
    background: linear-gradient(135deg, var(--card-dark), var(--card-darker));
    box-shadow: 0 6px 18px rgba(0,0,0,.18);
  }
  .card--front { left: 320px; top: 76px; }
  .card--back  { left: 320px; top: 530px; }

  /* Front */
  .gym-backdrop {
    position: absolute; inset: 0;
    background: radial-gradient(ellipse at 60% 35%, #3a3a3a 0%, #242424 55%, #171717 100%);
  }
  .brand {
    position: absolute; left: 0; right: 0; top: 118px;
    text-align: center; color: var(--white);
  }
  .brand__name {
    font-weight: 400; font-size: 46px; letter-spacing: 1px; line-height: 1;
    display: inline-flex; align-items: center; gap: 14px;
  }
  .brand__mark { width: 30px; height: 30px; background: var(--white); }
  .brand__role {
    margin-top: 10px; display: flex; align-items: center; justify-content: center; gap: 12px;
    font-weight: 300; font-size: 15px; letter-spacing: 5px;
  }
  .brand__role::before, .brand__role::after {
    content: ""; width: 70px; height: 1px; background: var(--white);
  }
  .web-band {
    position: absolute; left: 0; right: 0; top: 282px; height: 38px;
    background: var(--accent);
    display: flex; align-items: center; justify-content: center;
    color: var(--white); font-size: 19px; letter-spacing: 1px; font-weight: 400;
  }
  .web-band strong { font-weight: 700; }

  /* Back */
  .back-art { position: absolute; inset: 0; }
  .portrait {
    position: absolute; left: 34px; top: 52px; width: 150px; height: 310px;
    border-radius: 60px 60px 0 0;
    background: linear-gradient(180deg, var(--photo-mid), var(--photo-dark));
  }
  .back-header {
    position: absolute; left: 248px; top: 28px; color: var(--white); text-align: center;
  }
  .back-header__name { font-size: 27px; font-weight: 400; letter-spacing: .5px; line-height: 1; }
  .back-header__role {
    margin-top: 5px; display: flex; align-items: center; gap: 8px;
    font-size: 10px; font-weight: 300; letter-spacing: 3.5px;
  }
  .back-header__role::before, .back-header__role::after {
    content: ""; flex: 1; height: 1px; background: var(--white);
  }
  .contact {
    position: absolute; left: 262px; color: var(--text-light);
    font-size: 17px; font-weight: 400; line-height: 1.3;
  }
  .contact--web { top: 110px; color: var(--accent); font-size: 18px; }
  .contact--web strong { font-weight: 700; }
  .contact--mail { top: 152px; }
  .contact--phone { top: 192px; }
  .contact--address { top: 232px; }
</style>
</head>
<body>
<div class="canvas">

  <section class="card card--front" aria-label="Visitenkarte Vorderseite">
    <div class="gym-backdrop" role="img" aria-label="Dunkles Foto von Fitnessgeräten und Hanteln im Hintergrund"></div>
    <div class="brand">
      <div class="brand__name"><span class="brand__mark"></span>TOBIAS KELLINGER</div>
      <div class="brand__role">PERSONAL TRAINER</div>
    </div>
    <div class="web-band">www.<strong>kellinger-training</strong>.de</div>
  </section>

  <section class="card card--back" aria-label="Visitenkarte Rückseite">
    <svg class="back-art" width="560" height="362" viewBox="0 0 560 362" aria-hidden="true">
      <defs>
        <pattern id="stripes" width="16" height="362" patternUnits="userSpaceOnUse">
          <rect width="16" height="362" fill="var(--accent)"/>
          <rect width="7" height="362" fill="var(--accent-light)"/>
        </pattern>
      </defs>
      <polygon points="0,0 228,0 190,362 0,362" fill="url(#stripes)"/>
      <g fill="var(--accent)">
        <rect x="214" y="118" width="38" height="34"/>
        <rect x="210" y="158" width="38" height="34"/>
        <rect x="206" y="198" width="38" height="34"/>
        <rect x="202" y="238" width="38" height="34"/>
      </g>
      <g fill="none" stroke="var(--white)" stroke-width="1.6">
        <!-- globe -->
        <circle cx="233" cy="135" r="10"/>
        <ellipse cx="233" cy="135" rx="4.5" ry="10"/>
        <line x1="223" y1="135" x2="243" y2="135"/>
        <line x1="225" y1="130" x2="241" y2="130"/>
        <line x1="225" y1="140" x2="241" y2="140"/>
        <!-- mail -->
        <rect x="219" y="168" width="20" height="14"/>
        <polyline points="219,168 229,176 239,168"/>
        <!-- phone -->
        <path d="M218 206 q-2 4 3 11 q6 8 11 8 l3 -3 -5 -4 -3 2 q-4 -2 -6 -7 l2 -3 -4 -5 z"/>
        <!-- pin -->
        <path d="M221 265 q-8 -9 -8 -14 a8 8 0 0 1 16 0 q0 5 -8 14 z"/>
        <circle cx="221" cy="251" r="3"/>
      </g>
    </svg>
    <div class="portrait" role="img" aria-label="Schwarzweiß-Porträt des Trainers mit verschränkten Armen"></div>
    <div class="back-header">
      <div class="back-header__name">TOBIAS KELLINGER</div>
      <div class="back-header__role">PERSONAL TRAINER</div>
    </div>
    <div class="contact contact--web">www.<strong>kellinger-training</strong>.de</div>
    <div class="contact contact--mail">t.kellinger@mailbox.de</div>
    <div class="contact contact--phone">0163/2918374</div>
    <div class="contact contact--address">Tobias Kellinger<br>Lindenfeldweg 14<br>80412 München</div>
  </section>

</div>
</body>
</html>
```